Service Plan Sales Flyer

The Watchpost Depot (www.kelvamart.com) is a commercial security integrator that installs security cameras, access control, intrusion, two-way radios and perimeter security. We require a one page flyer for our service plan for new and existing customers. The price of the service plan is $299/yr and includes the following;
1. Discounted service rate of $118/hr
2. Free remote support ($85/hr without a plan)
3. Free remote training
4. Priority support

Please review our brochure attached and create a one page sales flyer with the end goal of having the client sign up for our annual service plan . The plan will automatically renew every year. Email sales@kelvamart.com.

Target Market(s)

commercial industrial clients - no residential

Industry/Entity Type

review our website at www.kelvamart.com

Colors
0054AA
0677BA
7BADD7
CADEEF
E8F1F8
EE7325
F08F49
F5BC92
FAE3D3
FDF4ED

Requirements
Must have
• call to action
Should not have
• too many colors

```html
<!DOCTYPE html>
<html lang="en">
<head>
<meta charset="utf-8">
<title>Watchpost Depot – Service Plan Flyer</title>
<link href="https://fonts.googleapis.com/css2?family=Bebas+Neue&family=Montserrat:wght@400;500;600;700&display=swap" rel="stylesheet">
<style>
  :root{
    --navy:#0d2b57;
    --navy-deep:#0b2550;
    --red:#e8443a;
    --red-dark:#c7302a;
    --paper:#f3f4f7;
    --ink:#1d2433;
    --white:#ffffff;
    --stage:#e9e9ec;
    --rule:#b9bcc4;
  }
  *{margin:0;padding:0;box-sizing:border-box}
  html,body{width:1200px;height:2400px;overflow:hidden;background:var(--stage)}
  .flyer{position:absolute;left:0;top:423px;width:1200px;height:1554px;background:linear-gradient(160deg,#f7f8fb 0%,var(--paper) 60%,#e9ebf0 100%);overflow:hidden;font-family:'Montserrat',sans-serif;color:var(--ink)}
  .shapes{position:absolute;inset:0}
  .brand{position:absolute;left:78px;top:62px;display:flex;align-items:center;gap:18px}
  .brand-mark{width:44px;height:44px;background:var(--navy)}
  .brand-name{font-family:'Bebas Neue',sans-serif;font-size:58px;line-height:1;color:var(--navy);letter-spacing:1px}
  .headline{position:absolute;left:80px;top:180px;font-family:'Bebas Neue',sans-serif;font-size:104px;line-height:80px;color:var(--navy);letter-spacing:1px}
  .section-title{position:absolute;left:81px;font-family:'Bebas Neue',sans-serif;font-size:44px;color:var(--red);letter-spacing:.5px}
  .section-title::after{content:"";position:absolute;left:0;bottom:-6px;width:46px;height:3px;background:var(--rule)}
  .about-title{top:470px}
  .products-title{top:832px}
  .about-text{position:absolute;left:81px;top:543px;width:480px;font-size:17.5px;line-height:21px;color:var(--ink)}
  .about-text p+p{margin-top:21px}
  .keypad-photo{position:absolute;left:0;top:918px;width:260px;height:496px;background:linear-gradient(100deg,#c9ccd2 0%,#e4e6ea 55%,rgba(243,244,247,0) 100%)}
  .product{position:absolute;left:277px;display:flex;align-items:center;gap:18px}
  .product-icon{width:90px;height:90px}
  .product-label{font-size:17.5px;line-height:21px;color:var(--ink)}
  .price{position:absolute;left:644px;top:280px;color:var(--white)}
  .price-lead{font-weight:600;font-size:44px;line-height:48px;letter-spacing:1px}
  .price-amount{font-family:'Bebas Neue',sans-serif;font-size:158px;line-height:1;margin-top:4px;letter-spacing:1px;display:flex;align-items:flex-start}
  .price-amount .currency{font-size:64px;margin-top:22px;margin-right:8px}
  .product-photo{position:absolute;left:684px;top:632px;width:470px;height:286px;background:radial-gradient(ellipse at 55% 50%,#f4f5f7 0%,#dfe2e8 45%,rgba(223,226,232,0) 72%)}
  .benefits{position:absolute;left:730px;top:985px;width:420px;list-style:none;color:var(--white)}
  .benefit{position:relative;padding-left:48px;font-weight:500;font-size:24px;line-height:30px;letter-spacing:.5px;text-transform:uppercase}
  .benefit svg{position:absolute;left:0;top:2px;width:32px;height:32px}
  .benefit-rule{height:0;border-top:3px dotted rgba(255,255,255,.45);margin:0 0 0 48px;width:340px}
  .contact-bar{position:absolute;left:0;top:1414px;width:1200px;height:140px;background:var(--red);color:var(--white)}
  .phone{position:absolute;left:96px;top:34px;display:flex;align-items:center;gap:14px;font-family:'Bebas Neue',sans-serif;font-size:78px;line-height:1}
  .phone svg{width:40px;height:40px}
  .divider{position:absolute;left:601px;top:26px;width:2px;height:88px;background:rgba(255,255,255,.85)}
  .online{position:absolute;left:665px;top:36px;font-size:26px;line-height:39px}
  .online div{display:flex;align-items:center;gap:16px}
  .online svg{width:26px;height:26px}
</style>
</head>
<body>
<main class="flyer">
  <svg class="shapes" viewBox="0 0 1200 1554" aria-hidden="true">
    <rect class="navy-panel" x="639" y="300" width="561" height="1114" fill="#0d2b57"/>
    <polygon class="red-arrow" points="1136,0 1200,0 1200,826 639,562 445,465 445,337" fill="#d83a33"/>
    <polygon points="1136,0 1200,0 1200,826 900,685" fill="#c7302a" opacity=".5"/>
  </svg>

  <div class="brand">
    <div class="brand-mark"></div>
    <div class="brand-name">THE WATCHPOST DEPOT</div>
  </div>

  <h1 class="headline">KNOWLEDGEABLE<br>RELIABLE<br>EASY</h1>

  <h2 class="section-title about-title">ABOUT US</h2>
  <div class="about-text">
    <p>From it's humble beginning in 1999, The Watchpost Depot Employees have worked hard to become one of Canada's most trusted commercial security integrators.</p>
    <p>We started 20 years ago when businesses still used VCR tapes to record their terrible grainy video for the entire day. Now we are called on by the smartest clients (that's you) to install high definition camera systems, card swipe access control, alarm systems and intercoms ... all accessible on their phones, tablets and PC.</p>
  </div>

  <h2 class="section-title products-title">PRODUCTS</h2>
  <div class="keypad-photo" role="img" aria-label="Photo of a hand holding a key card to a wall-mounted access control keypad"></div>

  <div class="product" style="top:906px">
    <svg class="product-icon" viewBox="0 0 90 90"><circle cx="45" cy="45" r="42" fill="#fff" stroke="#e8443a" stroke-width="3"/><rect x="26" y="38" width="34" height="16" rx="2" fill="#e8443a"/><rect x="58" y="42" width="8" height="8" fill="#e8443a"/><rect x="38" y="24" width="4" height="14" fill="#e8443a"/></svg>
    <div class="product-label">Security Camera<br>System</div>
  </div>
  <div class="product" style="top:1022px">
    <svg class="product-icon" viewBox="0 0 90 90"><circle cx="45" cy="45" r="42" fill="#fff" stroke="#e8443a" stroke-width="3"/><line x1="16" y1="16" x2="74" y2="74" stroke="#e8443a" stroke-width="3"/><circle cx="55" cy="35" r="9" fill="#e8443a"/><line x1="48" y1="42" x2="28" y2="62" stroke="#e8443a" stroke-width="5"/><line x1="32" y1="58" x2="38" y2="64" stroke="#e8443a" stroke-width="4"/></svg>
    <div class="product-label">Access Control<br>&amp; Intercom</div>
  </div>
  <div class="product" style="top:1143px">
    <svg class="product-icon" viewBox="0 0 90 90"><circle cx="45" cy="45" r="42" fill="#fff" stroke="#e8443a" stroke-width="3"/><rect x="29" y="24" width="32" height="42" rx="3" fill="none" stroke="#e8443a" stroke-width="3"/><rect x="34" y="29" width="22" height="8" fill="#e8443a"/><g fill="#e8443a"><rect x="34" y="42" width="5" height="5"/><rect x="42" y="42" width="5" height="5"/><rect x="50" y="42" width="5" height="5"/><rect x="34" y="51" width="5" height="5"/><rect x="42" y="51" width="5" height="5"/><rect x="50" y="51" width="5" height="5"/></g></svg>
    <div class="product-label">Intrusion<br>Alarm</div>
  </div>
  <div class="product" style="top:1263px">
    <svg class="product-icon" viewBox="0 0 90 90"><circle cx="45" cy="45" r="42" fill="#fff" stroke="#e8443a" stroke-width="3"/><g stroke="#e8443a" stroke-width="3" fill="none"><line x1="22" y1="34" x2="22" y2="64"/><line x1="32" y1="34" x2="32" y2="64"/><line x1="42" y1="34" x2="42" y2="64"/><line x1="18" y1="42" x2="50" y2="42"/><line x1="18" y1="54" x2="50" y2="54"/></g><path d="M60 30 L72 35 L72 48 Q72 58 60 64 Q48 58 48 48 L48 35 Z" fill="#e8443a"/></svg>
    <div class="product-label">Perimeter<br>Security</div>
  </div>

  <div class="price">
    <div class="price-lead">THE PRICE OF THE<br>SERVICE PLAN IS</div>
    <div class="price-amount"><span class="currency">$</span>299/YRY</div>
  </div>

  <div class="product-photo" role="img" aria-label="Product photo of a door, a monitor showing camera footage, and dome and bullet security cameras"></div>

  <ul class="benefits">
    <li class="benefit"><svg viewBox="0 0 32 32"><circle cx="16" cy="16" r="12" fill="none" stroke="#fff" stroke-width="2"/><path d="M10 16 L15 21 L27 8" fill="none" stroke="#fff" stroke-width="2.5"/></svg>Discounted service<br>rate of $118/hr</li>
    <li class="benefit-rule" style="margin-top:18px;margin-bottom:28px"></li>
    <li class="benefit"><svg viewBox="0 0 32 32"><circle cx="16" cy="16" r="12" fill="none" stroke="#fff" stroke-width="2"/><path d="M10 16 L15 21 L27 8" fill="none" stroke="#fff" stroke-width="2.5"/></svg>Free remote support<br>($85/hr without a plan)</li>
    <li class="benefit-rule" style="margin-top:36px;margin-bottom:36px"></li>
    <li class="benefit"><svg viewBox="0 0 32 32"><circle cx="16" cy="16" r="12" fill="none" stroke="#fff" stroke-width="2"/><path d="M10 16 L15 21 L27 8" fill="none" stroke="#fff" stroke-width="2.5"/></svg>Free remote training</li>
    <li class="benefit-rule" style="margin-top:22px;margin-bottom:24px"></li>
    <li class="benefit"><svg viewBox="0 0 32 32"><circle cx="16" cy="16" r="12" fill="none" stroke="#fff" stroke-width="2"/><path d="M10 16 L15 21 L27 8" fill="none" stroke="#fff" stroke-width="2.5"/></svg>Priority support</li>
  </ul>

  <footer class="contact-bar">
    <div class="phone">
      <svg viewBox="0 0 40 40"><path d="M12 6 L17 13 L13 17 Q17 24 23 27 L27 23 L34 28 L30 34 Q16 33 6 16 Z" fill="none" stroke="#fff" stroke-width="2.5" stroke-linejoin="round"/></svg>
      1-877-555-0142
    </div>
    <div class="divider"></div>
    <div class="online">
      <div><svg viewBox="0 0 26 26"><rect x="2" y="5" width="22" height="16" fill="none" stroke="#fff" stroke-width="2"/><path d="M2 5 L13 14 L24 5" fill="none" stroke="#fff" stroke-width="2"/></svg>Email sales@kelvamart.com.</div>
      <div><svg viewBox="0 0 26 26"><g fill="none" stroke="#fff" stroke-width="2"><circle cx="13" cy="13" r="10"/><ellipse cx="13" cy="13" rx="4.5" ry="10"/><line x1="3" y1="13" x2="23" y2="13"/></g></svg>www.kelvamart.com</div>
    </div>
  </footer>
</main>
</body>
</html>
```